Northwind Crate Traders Needs a FRESH website

We would like a creative minded designer to take on the task to Re-design our website. Its a simple 5-7 pages. With no cart, no complex html. Just plain information about our company and products we import and export. Pictures added to the product section. Since Our logo its Blue, we would like the designer to use complementing colors in order to make the website look cleaner and modern.

Target Market(s)

The target audience will be companies looking to purchase plastic related products. Companies looking to purchase large quantities of plastic containers (Shampoo bottles, caps, sprayers, mist sprayers, cosmetic containers etc).

Industry/Entity Type

It Company

Font styles to use
Sans Serif

Requirements
Must have
• We have a section in which we would like to add pictures of some of the products we carry, therefore having an easy and clean way to navigate through the pictures will be a plus.

```html
<!DOCTYPE html>
<html lang="en">
<head>
<meta charset="utf-8">
<title>Northwind Crate Traders</title>
<link rel="stylesheet" href="https://fonts.googleapis.com/css2?family=Open+Sans:wght@400;600;700&display=swap">
<style>
:root{
  --blue:#1a80c4;
  --blue-bright:#1ea2e4;
  --ink:#333;
  --text:#555;
  --muted:#777;
  --band:#e6e7e8;
  --footer-bar:#3a3b3d;
  --white:#fff;
}
*{box-sizing:border-box;margin:0;padding:0}
html,body{width:803px;height:1200px;overflow:hidden;background:var(--white)}
body{position:relative;font-family:"Open Sans",Arial,sans-serif;color:var(--text)}
.abs{position:absolute}

/* header */
.site-header{position:absolute;left:0;top:0;width:803px;height:56px;background:var(--white);z-index:3}
.brand-badge{position:absolute;left:53px;top:-66px;width:144px;height:144px;background:var(--blue-bright);transform:rotate(45deg);z-index:4;box-shadow:0 2px 0 rgba(0,0,0,.08)}
.brand-name{position:absolute;left:82px;top:30px;width:92px;z-index:5;color:var(--white);font-weight:700;font-size:12px;line-height:14px;text-align:center}
.main-nav{position:absolute;top:21px;left:0;width:803px;list-style:none;font-size:12.5px;color:var(--ink)}
.main-nav li{position:absolute;letter-spacing:.2px}
.main-nav .current::after{content:"";position:absolute;left:50%;top:19px;width:5px;height:5px;border-right:2px solid var(--blue-bright);border-bottom:2px solid var(--blue-bright);transform:translateX(-50%) rotate(45deg)}

/* hero */
.hero{position:absolute;left:0;top:56px;width:803px;height:356px;background:radial-gradient(ellipse at 68% 55%,#b98a74 0%,#6b5a52 18%,#2c2c2c 42%,#1b1b1b 100%)}
.hero-next{position:absolute;right:22px;top:168px}
.hero-caption{position:absolute;left:277px;top:276px;width:526px;height:51px;background:rgba(40,40,40,.55);color:var(--white);font-size:24px;line-height:51px;padding-left:6px;letter-spacing:.3px}

/* headings */
.section-title{position:absolute;color:var(--blue);font-weight:400;font-size:21.5px;line-height:26px}

/* welcome */
.welcome-photo{left:53px;top:491px;width:159px;height:160px;background:linear-gradient(135deg,#7a3a66 0%,#e0452e 35%,#f05a3c 65%,#c8322a 100%)}
.welcome-copy{left:235px;top:487px;width:218px;font-size:10.5px;line-height:17px;color:var(--text)}
.welcome-copy p+p{margin-top:6px}

/* news */
.news-list{left:519px;top:487px;width:240px;list-style:none}
.news-item{position:relative;height:60px}
.news-thumb{position:absolute;left:0;top:0;width:66px;height:46px}
.news-title{position:absolute;left:80px;top:0;font-size:10.5px;font-weight:700;color:var(--blue-bright);white-space:nowrap}
.news-text{position:absolute;left:80px;top:16px;width:160px;font-size:9.5px;line-height:15px;color:var(--text)}

/* products */
.products-band{left:0;top:747px;width:803px;height:243px;background:var(--band)}
.product{position:absolute;width:240px}
.product-icon{position:absolute;left:0;top:0;width:45px;height:45px;border-radius:50%;background:var(--blue)}
.product-name{position:absolute;left:60px;top:-6px;font-size:16px;color:var(--blue);white-space:nowrap;font-weight:400}
.product-text{position:absolute;left:60px;top:16px;width:180px;font-size:10.5px;line-height:17px;color:var(--text)}

/* footer */
.footer-col{position:absolute;top:1014px}
.footer-col h3{font-weight:400;font-size:15px;color:var(--ink);margin-bottom:10px}
.footer-links{list-style:none;font-size:10.5px;color:var(--text)}
.footer-links li{height:23px;padding-left:14px;position:relative}
.footer-links li::before{content:"";position:absolute;left:2px;top:6px;width:5px;height:5px;border-radius:50%;background:#999}
.contact-list{list-style:none;font-size:10.5px;color:var(--text)}
.contact-list li{position:relative;padding-left:22px;line-height:20px}
.contact-list svg{position:absolute;left:0;top:4px}
.follow-text{font-size:10.5px;line-height:17px;color:var(--muted);width:200px}
.social{display:flex;gap:6px;margin-top:10px}
.social span{width:24px;height:24px;border-radius:50%}
.social .s1{background:#3b5b9a}.social .s2{background:#39a9e0}.social .s3{background:#f07c1e}
.copyright-bar{left:0;top:1158px;width:803px;height:42px;background:var(--footer-bar);color:#ddd;font-size:10px;line-height:42px;padding-left:53px}
</style>
</head>
<body>

<header class="site-header">
  <ul class="main-nav">
    <li class="current" style="left:369px">HOME</li>
    <li style="left:435px">ABOUT US</li>
    <li style="left:523px">PRODUCTS</li>
    <li style="left:614px">MISSION</li>
    <li style="left:693px">CONTACT</li>
  </ul>
</header>
<div class="brand-badge"></div>
<div class="brand-name">Northwind Crate Traders</div>

<section class="hero" role="img" aria-label="Hand pouring black plastic resin pellets onto a pile of pellets">
  <svg class="hero-next" width="20" height="40" viewBox="0 0 20 40"><path d="M3 3 L17 20 L3 37" fill="none" stroke="rgba(255,255,255,.35)" stroke-width="3"/></svg>
  <div class="hero-caption">DUIS AUTEM VEL EUM IRIURE DOLORIN</div>
</section>

<h2 class="section-title" style="left:53px;top:446px">Welcome to Our Website</h2>
<div class="abs welcome-photo" role="img" aria-label="Hands sorting a bin of red plastic caps"></div>
<div class="abs welcome-copy">
  <p>Eu tortor euismodolo. Vestibulum ant psu meiop uere cubil. Cura sed quis nibhut odiocinialor mats ed iaculis ante sed vel laciniate. Eu tortor euismo dolo. Vestibulum ant psu meop primis inicibuo.</p>
  <p>Eu tortor euismodolo. Vestibulum ant psu meiop primis inicibu orci luctus ed ultrices et posuerecu bil. Cura sed quis nibhut odiocinialor matis ed iac ulis ante sed vel laciniate. Eu tortor euismodolo. Vestibulum ant psu meiop primis inicibu orci luct us ed ultrices et posuere cubil.</p>
</div>

<h2 class="section-title" style="left:515px;top:446px">Latest News</h2>
<ul class="abs news-list">
  <li class="news-item">
    <div class="news-thumb" role="img" aria-label="Cupped hands holding dark pellets" style="background:linear-gradient(135deg,#2a2a2a,#8a6a58 55%,#333)"></div>
    <span class="news-title">Duis autem vel eum iriure dolor</span>
    <p class="news-text">Brianne craves the endorphin rush fu eled by fitness and uses it.</p>
  </li>
  <li class="news-item">
    <div class="news-thumb" role="img" aria-label="Mixed coloured plastic flakes" style="background:linear-gradient(135deg,#d9cfc2,#c98f6a 40%,#9fb1c0 70%,#e2d6c6)"></div>
    <span class="news-title">Duis autem vel eum iriure dolor</span>
    <p class="news-text">Brianne craves the enindorphin rush fueled by fitness and uses it.</p>
  </li>
  <li class="news-item">
    <div class="news-thumb" role="img" aria-label="Coloured plastic granules" style="background:linear-gradient(135deg,#2b6fb0,#3aa7a0 40%,#e07a2a 75%,#c33b2a)"></div>
    <span class="news-title">Duis autem vel eum iriure dolor</span>
    <p class="news-text">Brianne craves the endinorphin rush fueled by fitness and uses it.</p>
  </li>
</ul>

<h2 class="section-title" style="left:0;top:699px;width:803px;text-align:center">Products</h2>
<section class="abs products-band">
  <div class="product" style="left:53px;top:43px">
    <svg class="product-icon" viewBox="0 0 45 45"><circle cx="22.5" cy="22.5" r="22.5" fill="#1a80c4"/><path d="M20 11h5v4c2 1 3 3 3 5v13c0 1-1 2-2 2h-7c-1 0-2-1-2-2V20c0-2 1-4 3-5z" fill="#fff"/></svg>
    <h3 class="product-name">PET</h3>
    <p class="product-text">Scing elit vivamus faucibus, mi quis convallisto tempus, magna elit.</p>
  </div>
  <div class="product" style="left:293px;top:43px">
    <svg class="product-icon" viewBox="0 0 45 45"><circle cx="22.5" cy="22.5" r="22.5" fill="#1a80c4"/><path d="M22.5 12l5 8M30 24l-4 8H19M15 28l5-9" fill="none" stroke="#fff" stroke-width="2.5" stroke-linecap="round"/><path d="M26 17l2 4-4 0zM17 32l-3-3 4-1zM31 27l-1 4-3-2z" fill="#fff"/></svg>
    <h3 class="product-name">PET RESIN</h3>
    <p class="product-text">Scing elit vivamus faucibus, mi quis convallisto tempus, magna elit.</p>
  </div>
  <div class="product" style="left:538px;top:43px">
    <svg class="product-icon" viewBox="0 0 45 45"><circle cx="22.5" cy="22.5" r="22.5" fill="#1a80c4"/><g transform="rotate(40 22.5 22.5)"><rect x="18" y="13" width="9" height="20" rx="2" fill="#fff"/><rect x="19.5" y="9" width="6" height="4" fill="#fff"/><path d="M19 19h7M19 23h7" stroke="#1a80c4" stroke-width="1.2"/></g></svg>
    <h3 class="product-name">PET CONTAINERS</h3>
    <p class="product-text">Scing elit vivamus faucibus, mi qus convallisto tempus, magna elit.</p>
  </div>
  <div class="product" style="left:53px;top:139px">
    <svg class="product-icon" viewBox="0 0 45 45"><circle cx="22.5" cy="22.5" r="22.5" fill="#1a80c4"/><rect x="19" y="10" width="7" height="4" fill="#fff"/><rect x="17" y="15" width="11" height="20" rx="2" fill="#fff"/></svg>
    <h3 class="product-name">P.E.P.P. Containers</h3>
    <p class="product-text">Scing elit vivamus faucibus, mi quis convallisto tempus, magna elit.</p>
  </div>
  <div class="product" style="left:293px;top:139px">
    <svg class="product-icon" viewBox="0 0 45 45"><circle cx="22.5" cy="22.5" r="22.5" fill="#1a80c4"/><path d="M19 10h6v3h3v3h-9zM18 17h9v17c0 1-1 2-2 2h-5c-1 0-2-1-2-2z" fill="#fff"/></svg>
    <h3 class="product-name">SPRAYERS</h3>
    <p class="product-text">Scing elit vivamus faucibus, mi quis convallisto tempus, magna elit.</p>
  </div>
  <div class="product" style="left:538px;top:139px">
    <svg class="product-icon" viewBox="0 0 45 45"><circle cx="22.5" cy="22.5" r="22.5" fill="#1a80c4"/><circle cx="22.5" cy="22.5" r="8" fill="none" stroke="#fff" stroke-width="4" stroke-dasharray="4 2.3"/><circle cx="22.5" cy="22.5" r="6" fill="none" stroke="#fff" stroke-width="2.5"/></svg>
    <h3 class="product-name">MOLDS</h3>
    <p class="product-text">Scing elit vivamus faucibus, mi qus convallisto tempus, magna elit.</p>
  </div>
</section>

<footer>
  <div class="footer-col" style="left:53px">
    <h3>Site Map</h3>
    <ul class="footer-links"><li>Home</li><li>About</li><li>Programs</li><li>Contact Us</li></ul>
  </div>
  <div class="footer-col" style="left:188px">
    <h3>Links</h3>
    <ul class="footer-links"><li>Consuetudium</li><li>Praesent luptum</li><li>Duis autem veum</li><li>Nam liber tempor</li></ul>
  </div>
  <div class="footer-col" style="left:351px">
    <h3>Contact</h3>
    <ul class="contact-list">
      <li><svg width="10" height="13" viewBox="0 0 10 13"><path d="M5 0a5 5 0 0 1 5 5c0 3-5 8-5 8S0 8 0 5a5 5 0 0 1 5-5z" fill="#444"/><circle cx="5" cy="5" r="2" fill="#fff"/></svg># 22, Harbor Row<br>58 Quayside Tce, SA 5190</li>
      <li><svg width="12" height="9" viewBox="0 0 12 9"><rect width="12" height="9" fill="#444"/><path d="M0 0l6 5 6-5" fill="none" stroke="#fff" stroke-width="1"/></svg>hello@northwindcrate.net</li>
      <li style="margin-top:2px"><svg width="11" height="11" viewBox="0 0 11 11"><path d="M2 0l2 3-1 1.5c.8 1.5 2 2.7 3.5 3.5L8 7l3 2-1 2C5 11 0 6 0 1z" fill="#444"/></svg>07 4410 2968</li>
    </ul>
  </div>
  <div class="footer-col" style="left:540px">
    <h3>Follow Us</h3>
    <p class="follow-text">Follow our news and events through social networks</p>
    <div class="social"><span class="s1"></span><span class="s2"></span><span class="s3"></span></div>
  </div>
  <div class="abs copyright-bar">Copyright © 2013. All Rights Reserved</div>
</footer>

</body>
</html>
```